LumaPeak business card

We are a performing arts company providing training (to both kids and adults) as well as performers for events. We hope to bring joy and confidence on stage to the people we train, as well as joy to the audience when our artistes perform. Designs should convey the joy, confidence and vibrancy on stage. Design business card using the attached logo. Card to include name, mobile tel, email address, company address, and website. Double sided. To also include the following list of what the company does:
• Training & Enrichment
• Private & Corporate Entertainment
- Music composition & production

Industry/Entity Type

Training

Contact Information for Business Card

Card to include name, mobile tel, email address, company address, and website. Double sided. To also include the following list of what the company does:
• Training & Enrichment

Requirements
Nice to have
• Card need not be the traditional rectangular in shape but not too outrageous.

```html
<!DOCTYPE html>
<html lang="en">
<head>
<meta charset="utf-8">
<title>LumaPeak business card</title>
<link rel="stylesheet" href="https://fonts.googleapis.com/css2?family=Arimo:wght@400&display=swap">
<style>
  :root {
    --page: #ffffff;
    --sky-light: #a9dbe6;
    --sky: #4fb0cc;
    --sky-deep: #23779a;
    --teal-text: #1a7f9e;
    --brand: #1d4f8c;
    --oval-light: #d6eefa;
    --oval: #6cc3ea;
  }
  * { margin: 0; padding: 0; box-sizing: border-box; }
  html, body { width: 1200px; height: 1000px; overflow: hidden; background: var(--page); }
  .canvas { position: relative; width: 1200px; height: 1000px; }
  .texture {
    position: absolute;
    background:
      linear-gradient(90deg, rgba(255,255,255,0.18) 0%, rgba(255,255,255,0) 20%, rgba(255,255,255,0.12) 45%, rgba(255,255,255,0) 70%, rgba(255,255,255,0.15) 100%),
      linear-gradient(180deg, var(--sky-light) 0%, var(--sky) 40%, var(--sky-deep) 100%);
  }
  .card { position: absolute; left: 232px; width: 735px; height: 420px; overflow: hidden; }
  .card-front { top: 65px; }
  .card-front .texture { inset: 0;
    background:
      linear-gradient(180deg, rgba(255,255,255,0) 0%, rgba(255,255,255,0.1) 30%, rgba(0,60,90,0.08) 55%, rgba(255,255,255,0.12) 80%, rgba(0,60,90,0.1) 100%),
      radial-gradient(ellipse at 55% 30%, #9fd6e4 0%, var(--sky) 45%, var(--sky-deep) 100%); }
  .oval { position: absolute; left: 0; top: 0; }
  .brand-name { position: absolute; text-align: center; white-space: nowrap;
    font: 400 50px "Arimo", sans-serif; color: var(--brand); letter-spacing: -0.5px; }
  .front-name { left: 0; width: 735px; top: 200px; }

  .card-back { top: 520px; background: var(--page); }
  .band-top { left: 0; top: 0; width: 735px; height: 33px; }
  .band-top-left { left: 0; top: 33px; width: 178px; height: 19px; }
  .strip-top { left: 178px; top: 52px; width: 557px; height: 13px; }
  .strip-bottom { left: 178px; top: 353px; width: 557px; height: 14px; }
  .band-bottom-left { left: 0; top: 367px; width: 178px; height: 20px; }
  .band-bottom { left: 0; top: 387px; width: 735px; height: 33px; }
  .edge-line { position: absolute; left: 734px; top: 65px; width: 1px; height: 288px; background: var(--sky); }

  .back-name { left: 28px; top: 212px; width: 244px; }

  .services { position: absolute; list-style: none; font: 400 28px "Arimo", sans-serif;
    font-variant: small-caps; color: var(--teal-text); }
  .services li { position: absolute; white-space: nowrap; }
  .services li:nth-child(1) { left: 190px; top: 84px; }
  .services li:nth-child(2) { left: 245px; top: 120px; }
  .services li:nth-child(3) { left: 290px; top: 155px; }

  .contact { position: absolute; left: 368px; top: 208px; list-style: none;
    font: 400 22px "Arimo", sans-serif; font-variant: small-caps; color: var(--teal-text); line-height: 28px; }
</style>
</head>
<body>
<main class="canvas">
  <section class="card card-front">
    <div class="texture" role="img" aria-label="Soft blurred blue stage-light backdrop"></div>
    <svg class="oval" width="735" height="420" aria-hidden="true">
      <defs>
        <linearGradient id="ovalFill" x1="0" y1="0" x2="1" y2="1">
          <stop offset="0" stop-color="var(--oval)"/>
          <stop offset="1" stop-color="var(--oval-light)"/>
        </linearGradient>
      </defs>
      <ellipse cx="360" cy="228" rx="148" ry="80" transform="rotate(18 360 228)" fill="url(#ovalFill)"/>
    </svg>
    <div class="brand-name front-name">LumaPeak</div>
  </section>

  <section class="card card-back">
    <div class="texture band-top" role="img" aria-label="Blurred blue backdrop band"></div>
    <div class="texture band-top-left"></div>
    <div class="texture strip-top"></div>
    <div class="edge-line"></div>
    <div class="texture strip-bottom"></div>
    <div class="texture band-bottom-left"></div>
    <div class="texture band-bottom" role="img" aria-label="Blurred blue backdrop band"></div>

    <div class="brand-name back-name">LumaPeak</div>

    <ul class="services">
      <li>Training &amp; Enrichment</li>
      <li>Private &amp; Corporate Entertainment</li>
      <li>Music Composition &amp; Production</li>
    </ul>

    <ul class="contact">
      <li>Name</li>
      <li>Email</li>
      <li>Address</li>
      <li>Phone</li>
      <li>Site</li>
    </ul>
  </section>
</main>
</body>
</html>
```